New Brand - Website Design (4 Pages)

We are launching a new brand for electronic cigarettes. We already have logo and packaging done and would like a web design to go with it.

We are interested in the following deliverables:

1) Home Page Design
2) Check Out Design
3) How it Works Page
4) Secondary Template Page Design

Looking for a 60s modern look and something that is consistent with our logo and packaging.

Industry/Entity Type

Electronic

Requirements
Must have
• Consistent with logo and packaging (Use Logo Attached)
White background

Example (Functionality & Design): http://www.torvex.co.uk/
Example (Design): http://www.quillharbor.com/

We want the design more like quillharbor but the functionality the same as torvex.

Top Bar: Pebble Arcs Kits; Cartridge Refills; How it Works; Contact; My Account; Checkout
Should not have
• Stock List or Search Bar or Newsletter Signup

```html
<!DOCTYPE html>
<html lang="en">
<head>
<meta charset="utf-8">
<title>Pebble Arcs</title>
<link href="https://fonts.googleapis.com/css2?family=Signika:wght@300;400&family=PT+Serif&display=swap" rel="stylesheet">
<style>
:root{
  --ink:#1d1d1d;
  --paper:#ffffff;
  --blue:#5aa6d3;
  --pale-blue:#a9d3ee;
  --red:#c9513c;
  --text:#5b5b5b;
  --rule:#d8d8d8;
  --footer-text:#c8c8c8;
}
*{margin:0;padding:0;box-sizing:border-box}
html,body{width:1034px;height:1200px;overflow:hidden;background:var(--paper)}
body{position:relative;font-family:"Signika",sans-serif;font-weight:300;color:var(--text)}
.abs{position:absolute}

.site-header{left:0;top:0;width:1034px;height:119px;background:var(--ink)}
.brand{left:87px;top:20px;display:flex;align-items:center;gap:12px}
.brand-dot{width:76px;height:76px;border-radius:50%;background:var(--pale-blue)}
.brand-name{color:#fff;font-size:30px;font-weight:400;letter-spacing:2px}
.account{left:673px;top:34px;color:#fff;font-size:12px;display:flex;align-items:center;gap:6px}
.cart{left:780px;top:25px;width:168px;height:29px;background:#fff;border-radius:3px;font-size:12px;color:#333;display:flex;align-items:center;gap:6px;padding-left:10px}
.cart b{color:var(--blue);font-weight:400}
.main-nav{right:86px;top:86px;display:flex;gap:28px;font-size:13px;color:#fff}
.main-nav span{position:relative;padding:0 3px}
.main-nav .active{color:var(--pale-blue)}
.main-nav .active::after{content:"";position:absolute;left:0;right:0;top:27px;height:4px;background:var(--pale-blue)}

.hero{left:85px;top:135px;width:864px;height:334px;background:linear-gradient(90deg,#c3dbe4 0%,#d9e9ef 45%,#9fb7c6 62%,#2c3f55 75%,#07121f 100%)}
.hero-title{left:145px;top:174px;width:288px;border-top:1px solid #777;border-bottom:4px solid #777;font-family:"PT Serif",serif;font-weight:400;font-size:28px;line-height:36px;color:#333;text-align:center;padding:8px 0 9px;letter-spacing:0.5px;white-space:nowrap}
.buy-now{left:306px;top:248px;width:128px;height:41px;background:var(--red);color:#fff;font-family:"PT Serif",serif;font-size:19px;display:flex;align-items:center;justify-content:center;gap:12px}
.pack{left:106px;top:272px;width:178px;height:174px;background:linear-gradient(135deg,#3a2a26,#16100e 60%,#b9523f);border-radius:4px}

.card{top:486px;width:270px}
.card-photo{height:145px}
.card h2{font-weight:400;color:var(--blue);font-size:21px;margin-top:13px}
.card p{font-size:12.6px;line-height:20px;margin-top:8px}
.more{color:var(--red)}

.rule{left:86px;width:864px;height:1px;background:var(--rule)}

.why{left:95px;top:782px;width:558px}
.why h2,.how h2{font-weight:400;color:var(--blue);font-size:25px}
.why p{font-size:12.6px;line-height:20px;margin-top:8px}
.ticks{list-style:none;margin-top:12px}
.ticks li{color:var(--red);font-size:14.5px;height:30.6px;display:flex;align-items:center;gap:10px}
.sticks{left:497px;top:900px;width:145px;height:115px;background:linear-gradient(180deg,#f4f4f4,#8a8a8a 40%,#222 90%);border-radius:8px}
.how{left:670px;top:788px}
.how h2{font-size:21px}
.video{left:670px;top:828px;width:270px;height:175px;background:linear-gradient(90deg,#1a1512,#5a4538 50%,#2a211c)}
.play{left:104px;top:55px}

.quote{left:130px;top:1062px;width:800px;display:flex;align-items:center;gap:8px;font-size:21px;color:#444}
.quote .client{color:var(--blue);font-size:14.5px;margin-left:10px}
.quote-mark{color:#555;font-size:24px;font-weight:400}

.site-footer{left:0;top:1112px;width:1034px;height:88px;background:#2a2a2a}
.foot-nav{left:87px;top:1132px;font-size:12px;color:var(--footer-text);display:flex;gap:9px}
.copy{left:87px;top:1164px;font-size:12px;color:var(--footer-text)}
.social{left:836px;top:1144px;display:flex;gap:8px}
.social span{width:22px;height:22px;border-radius:50%;background:#666;display:flex;align-items:center;justify-content:center}
</style>
</head>
<body>

<header class="site-header abs"></header>
<div class="brand abs"><span class="brand-dot"></span><span class="brand-name">PEBBLE ARCS</span></div>
<div class="account abs">
  <svg width="12" height="12" viewBox="0 0 12 12"><circle cx="6" cy="3.5" r="3" fill="#ccc"/><path d="M0 12c0-4 3-5 6-5s6 1 6 5z" fill="#ccc"/></svg>
  MY ACCOUNT
</div>
<div class="cart abs">
  <svg width="20" height="16" viewBox="0 0 20 16" fill="none" stroke="#5aa6d3" stroke-width="1.4"><path d="M1 1h3l2 9h10l2-7H5"/><circle cx="8" cy="14" r="1.3"/><circle cx="15" cy="14" r="1.3"/></svg>
  <span><b>0</b> item(s) &nbsp;/&nbsp; Total : <b>$0.00</b></span>
</div>
<nav class="main-nav abs">
  <span class="active">PEBBLE ARCS KITS</span><span>CARTRIDGE REFILLS</span><span>HOW IT WORKS</span><span>CONTACT</span>
</nav>

<section class="hero abs" role="img" aria-label="Photo of a man in silhouette smoking an electronic cigarette with rising vapour"></section>
<div class="pack abs" role="img" aria-label="Product box with cartridges"></div>
<h1 class="hero-title abs">NULLAM &nbsp;PULVINAR</h1>
<a class="buy-now abs">Buy Now
  <svg width="12" height="12" viewBox="0 0 12 12"><circle cx="6" cy="6" r="6" fill="#fff"/><path d="M4.5 3.5 7 6 4.5 8.5" stroke="#c9513c" stroke-width="1.6" fill="none"/></svg>
</a>

<article class="card abs" style="left:94px">
  <div class="card-photo" role="img" aria-label="Photo of a woman exhaling vapour" style="background:linear-gradient(135deg,#0d1a33,#283c5c 50%,#0b0b0b)"></div>
  <h2>WELCOME</h2>
  <p>Sed massa nisl, mattis non hendrerit eu, tempus id libero. Cum sociis natoque penatibus et magnis dis parturient montes, nascetur. &nbsp;<span class="more">MORE</span></p>
</article>
<article class="card abs" style="left:382px">
  <div class="card-photo" role="img" aria-label="Photo of the starter kit boxes" style="background:linear-gradient(90deg,#e8e8e8,#2a2f3d 30%,#ececec 60%,#d6d6d6)"></div>
  <h2>PEBBLE ARCS KITS</h2>
  <p>Sed massa nisl, mattis non hendrerit eu, tempus id libero. Cum sociis natoque penatibus et magnis dis parturient montes, nascetur. &nbsp;<span class="more">MORE</span></p>
</article>
<article class="card abs" style="left:670px">
  <div class="card-photo" role="img" aria-label="Photo of loose orange refill cartridges" style="background:radial-gradient(circle at 55% 50%,#e8a060 0%,#f1d2b0 30%,#f1f1f1 60%)"></div>
  <h2>CARTRIDGE REFILLS</h2>
  <p>Sed massa nisl, mattis non hendrerit eu, tempus id libero. Cum sociis natoque penatibus et magnis dis parturient montes, nascetur. &nbsp;<span class="more">MORE</span></p>
</article>

<div class="rule abs" style="top:763px"></div>

<section class="why abs">
  <h2>WHY US?</h2>
  <p>Maecenas ac gravida massa. Donec quis purus et felis pretium sagittis. Donec tincidunt dui quam, et convallis magna commodo nec. Cras facilisis pulvinar nibh, quis gravida orci pharetra sit amet. Duis aliquam in diam sed tincidunt. Cras vel bibendum quam, in consequat sapien.</p>
  <ul class="ticks">
    <li><svg width="11" height="9" viewBox="0 0 11 9"><path d="M1 4.5 4 7.5 10 1" stroke="#c9513c" stroke-width="1.8" fill="none"/></svg>Integer sed lorem pharetra, eleifend metus</li>
    <li><svg width="11" height="9" viewBox="0 0 11 9"><path d="M1 4.5 4 7.5 10 1" stroke="#c9513c" stroke-width="1.8" fill="none"/></svg>Proin nec nisl quis tortor tempor cursus</li>
    <li><svg width="11" height="9" viewBox="0 0 11 9"><path d="M1 4.5 4 7.5 10 1" stroke="#c9513c" stroke-width="1.8" fill="none"/></svg>Suspendisse dui enim, commodo et velit nec</li>
    <li><svg width="11" height="9" viewBox="0 0 11 9"><path d="M1 4.5 4 7.5 10 1" stroke="#c9513c" stroke-width="1.8" fill="none"/></svg>Nullam sit amet ipsum sed enim</li>
  </ul>
</section>
<div class="sticks abs" role="img" aria-label="Photo of a fan of black e-cigarettes"></div>

<section class="how abs"><h2>HOW IT WORKS</h2></section>
<div class="video abs" role="img" aria-label="Video still of a woman using an electronic cigarette">
  <svg class="play abs" width="64" height="64" viewBox="0 0 64 64"><circle cx="32" cy="32" r="29" fill="none" stroke="#fff" stroke-width="4"/><path d="M25 18 47 32 25 46z" fill="#fff"/></svg>
</div>

<div class="rule abs" style="top:1040px"></div>

<blockquote class="quote abs">
  <span class="quote-mark">&ldquo;</span>
  Proin quis iaculis dui, sed scelerisque massa habitant morbi tristique.
  <span class="quote-mark">&rdquo;</span>
  <span class="client">- &nbsp;Client name, City</span>
</blockquote>

<footer class="site-footer abs"></footer>
<nav class="foot-nav abs">
  <span>Home</span><span>|</span><span>Pebble Arcs Kits</span><span>|</span><span>Cartridge Refills</span><span>|</span><span>How it Works</span><span>|</span><span>Contact</span><span>|</span><span>My Account</span><span>|</span><span>Checkout</span>
</nav>
<p class="copy abs">Copyright &copy; 2013 &nbsp;Pebble Arcs. &nbsp;All rights reserved.</p>
<div class="social abs">
  <span></span><span></span><span></span>
  <span><svg width="12" height="9" viewBox="0 0 12 9" fill="none" stroke="#2a2a2a" stroke-width="1.2"><rect x="0.6" y="0.6" width="10.8" height="7.8"/><path d="M0.6 0.6 6 5 11.4 0.6"/></svg></span>
</div>

</body>
</html>
```